Powerpoint Presentation design template

I am looking for a PPT presentation that show class and professionalism and in the same colour them as the logo. It should be simple, but yet classy and pro. The business is an oil and gas exploration and exploitation business. The business has nothing to do with solar panel and other renewable energies, so please no solar panel or wind farms in the background. It would be more oil rigs and LNG plant in the background of some slide templates...

oil and gas exploration and exploitation

```html
<!DOCTYPE html>
<html lang="en">
<head>
<meta charset="utf-8">
<title>Kestrel Energy – Presentation Template</title>
<link href="https://fonts.googleapis.com/css2?family=Poppins:wght@400;500;600;700;800&display=swap" rel="stylesheet">
<style>
:root{
  --green:#12a57c;
  --blue:#0a8dd6;
  --dark:#222426;
  --grey:#f1f2f3;
  --mid:#b9bcbf;
  --text:#8a8d90;
  --bg:#d9dadc;
}
*{box-sizing:border-box;margin:0;padding:0}
html,body{width:898px;height:1200px;overflow:hidden;background:var(--bg);font-family:'Poppins',sans-serif}
.board{position:relative;width:898px;height:1200px}
.slide{position:absolute;width:266px;height:150px;background:#fff;overflow:hidden;box-shadow:0 1px 3px rgba(0,0,0,.18)}
.a{position:absolute}
.eyebrow{position:absolute;color:var(--green);font-weight:600;font-size:8.5px;line-height:1;text-transform:uppercase}
.heading{position:absolute;color:var(--blue);font-weight:800;font-size:10.5px;line-height:1;text-transform:uppercase}
.kicker{position:absolute;color:var(--dark);font-weight:500;font-size:3.6px;text-transform:uppercase}
.tx{font-size:2.6px;line-height:1.4;color:var(--text)}
.tb{font-size:3.8px;font-weight:700;color:var(--dark);line-height:1.3}
.foot .brand{position:absolute;left:7px;top:138px;font-size:3.6px;font-weight:700;color:var(--blue);display:flex;align-items:center;gap:2px}
.dot{display:inline-block;border-radius:50%;background:var(--green)}
.foot .rule{position:absolute;left:40px;right:12px;top:142px;height:.4px;background:var(--blue)}
.foot .num{position:absolute;right:7px;top:140px;font-size:2.6px;color:var(--dark)}
.media{position:absolute;background:linear-gradient(135deg,#5e7f99,#c9a47a)}
.tick{display:inline-block;width:6px;height:6px;border-radius:50%;background:var(--green)}
table{border-collapse:collapse}
</style>
</head>
<body>
<div class="board">

<!-- 1 Cover -->
<section class="slide" style="left:36px;top:36px">
  <div class="a" style="left:14px;top:16px;display:flex;align-items:center;gap:3px">
    <span class="dot" style="width:13px;height:13px"></span>
    <span style="font-size:8px;font-weight:800;color:var(--blue);line-height:1">KESTREL<br>ENERGY</span>
  </div>
  <div class="a" style="left:13px;top:66px;font-size:14px;font-weight:800;color:var(--blue)">BUSINESS</div>
  <div class="a" style="left:13px;top:83px;font-size:5.5px;font-weight:700;color:var(--green)">Presentation Template</div>
  <div class="a tx" style="left:13px;top:92px;width:60px;color:#444">Lorem ipsum is simply dummy text of the printing and typesetting industry.</div>
  <div class="a" style="left:13px;top:134px;font-size:4.6px;letter-spacing:1.6px;color:var(--blue)">www.website.com</div>
  <div class="a" role="img" aria-label="Large soft green-to-blue brand decoration" style="left:112px;top:-12px;width:180px;height:176px;border-radius:50%;background:linear-gradient(150deg,#8fd13f 0%,#12a57c 45%,#3cb4e6 100%)"></div>
</section>

<!-- 2 Part One -->
<section class="slide" style="left:316px;top:36px">
  <div class="a" style="left:17px;top:15px;display:flex;align-items:center;gap:3px">
    <span class="dot" style="width:11px;height:11px"></span>
    <span style="font-size:6.5px;font-weight:800;color:var(--blue);line-height:1">KESTREL<br>ENERGY</span>
  </div>
  <div class="media" role="img" aria-label="Oil refinery towers at sunset" style="left:107px;top:10px;width:148px;height:128px;border-radius:30px 45px 0 30px;background:linear-gradient(180deg,#7d8fa8 0%,#c9a47e 45%,#5b5247 100%)"></div>
  <div class="a" style="left:16px;top:52px;width:4px;height:46px;background:var(--blue)"></div>
  <div class="a" style="left:20px;top:52px;width:116px;height:46px;background:#fff"></div>
  <div class="a" style="left:30px;top:55px;font-size:16px;font-weight:800;color:var(--dark)">Part One</div>
  <div class="a tx" style="left:30px;top:78px;width:100px;font-size:3.4px;color:#555">Lorem ipsum dolor sit amet, laoreet dolore magna aliquam erat volutpat. Ut wisi it lob edo consequat. Ore te feugait nulla facilisi.</div>
  <div class="a" style="left:17px;top:124px;display:flex;align-items:center;gap:3px;font-size:3.4px;color:#555"><span class="dot" style="width:8px;height:8px"></span>Your Website Name Goes Here</div>
</section>

<!-- 3 Table of content -->
<section class="slide" style="left:596px;top:36px">
  <div class="a" style="left:25px;top:55px;font-size:8px;color:var(--blue);font-weight:500">TABLE OF</div>
  <div class="a" style="left:25px;top:63px;font-size:13px;font-weight:800;color:var(--green)">CONTENT</div>
  <div class="a tx" style="left:25px;top:80px;width:100px;font-size:3px;color:#555">Lorem Ipsum is simply dummy text of the printing and typesetting industry. Lorem Ipsum has been the industry's standard dummy text ever since the 1500s.</div>
  <div class="a" style="left:134px;top:33px;width:100px">
    <div style="display:grid;row-gap:7.6px">
      <div style="display:flex;align-items:center;gap:2px;font-size:3px;color:var(--dark);font-weight:500"><span class="dot" style="width:1.6px;height:1.6px;background:var(--blue)"></span>Simple Text One<span style="flex:1;border-bottom:.4px dotted var(--blue);margin:0 2px"></span><span style="width:7px;height:7px;border-radius:50%;background:var(--blue);color:#fff;font-size:3px;display:grid;place-items:center">02</span></div>
      <div style="display:flex;align-items:center;gap:2px;font-size:3px;color:var(--dark);font-weight:500"><span class="dot" style="width:1.6px;height:1.6px;background:var(--blue)"></span>Simple Text Two<span style="flex:1;border-bottom:.4px dotted var(--blue);margin:0 2px"></span><span style="width:7px;height:7px;border-radius:50%;background:var(--blue);color:#fff;font-size:3px;display:grid;place-items:center">04</span></div>
      <div style="display:flex;align-items:center;gap:2px;font-size:3px;color:var(--dark);font-weight:500"><span class="dot" style="width:1.6px;height:1.6px;background:var(--blue)"></span>Simple Text Three<span style="flex:1;border-bottom:.4px dotted var(--blue);margin:0 2px"></span><span style="width:7px;height:7px;border-radius:50%;background:var(--blue);color:#fff;font-size:3px;display:grid;place-items:center">06</span></div>
      <div style="display:flex;align-items:center;gap:2px;font-size:3px;color:var(--dark);font-weight:500"><span class="dot" style="width:1.6px;height:1.6px;background:var(--blue)"></span>Simple Text Four<span style="flex:1;border-bottom:.4px dotted var(--blue);margin:0 2px"></span><span style="width:7px;height:7px;border-radius:50%;background:var(--blue);color:#fff;font-size:3px;display:grid;place-items:center">08</span></div>
      <div style="display:flex;align-items:center;gap:2px;font-size:3px;color:var(--dark);font-weight:500"><span class="dot" style="width:1.6px;height:1.6px;background:var(--blue)"></span>Simple Text Five<span style="flex:1;border-bottom:.4px dotted var(--blue);margin:0 2px"></span><span style="width:7px;height:7px;border-radius:50%;background:var(--blue);color:#fff;font-size:3px;display:grid;place-items:center">10</span></div>
      <div style="display:flex;align-items:center;gap:2px;font-size:3px;color:var(--dark);font-weight:500"><span class="dot" style="width:1.6px;height:1.6px;background:var(--blue)"></span>Simple Text Six<span style="flex:1;border-bottom:.4px dotted var(--blue);margin:0 2px"></span><span style="width:7px;height:7px;border-radius:50%;background:var(--blue);color:#fff;font-size:3px;display:grid;place-items:center">12</span></div>
    </div>
  </div>
  <div class="foot"><div class="brand"><span class="dot" style="width:5px;height:5px"></span>KESTREL</div><div class="rule"></div><div class="num">2</div></div>
</section>

<!-- 4 Overview -->
<section class="slide" style="left:36px;top:199px">
  <div class="kicker" style="left:19px;top:14px">A Business Text Here</div>
  <div class="eyebrow" style="left:19px;top:25px">Overview of</div>
  <div class="heading" style="left:19px;top:35px;font-size:13px">Kestrel Energy</div>
  <div class="a" style="left:126px;top:0;width:140px;height:80px;background:var(--green);clip-path:polygon(0 0,12% 0,44% 100%,34% 100%)"></div>
  <div class="media" role="img" aria-label="Oil pumpjack with two engineers in hard hats" style="left:143px;top:0;width:123px;height:80px;clip-path:polygon(0 0,100% 0,100% 100%,33% 100%);background:linear-gradient(160deg,#e9ecef 0%,#b7bec6 55%,#3a3f45 100%)"></div>
  <div class="a tx" style="left:19px;top:51px;width:100px;font-size:3px;color:#555">Lorem ipsum dolor amet consectetur adipisc eiusmod incididunt labore dolore magna ullamco aliqua. Aliquip commodo consequat.</div>
  <div class="a" style="left:19px;top:79px;display:grid;row-gap:8px">
    <div style="display:flex;gap:6px;align-items:center"><span class="tick"></span><span class="tx" style="width:80px;color:#555">Lorem Ipsum is simply dummy text ofn the print and typesetting magna aliqua.</span></div>
    <div style="display:flex;gap:6px;align-items:center"><span class="tick"></span><span class="tx" style="width:80px;color:#555">Lorem Ipsum is simply dummy text ofn the print and typesetting magna aliqua.</span></div>
    <div style="display:flex;gap:6px;align-items:center"><span class="tick"></span><span class="tx" style="width:80px;color:#555">Lorem Ipsum is simply dummy text ofn the print and typesetting magna aliqua.</span></div>
  </div>
  <div class="a" style="left:130px;top:90px;width:60px">
    <div style="display:flex;align-items:center;gap:3px" class="tb"><span style="width:9px;height:9px;background:var(--blue);clip-path:polygon(50% 0,100% 25%,100% 75%,50% 100%,0 75%,0 25%)"></span><span style="font-size:3.3px">Write Simple Text</span></div>
    <div class="tx" style="margin-top:4px;color:#555">Lorem Ipsum is simply dummy text a print and typeset industry has text ever since the 1500s.</div>
  </div>
  <div class="a" style="left:196px;top:90px;width:60px">
    <div style="display:flex;align-items:center;gap:3px" class="tb"><span style="width:9px;height:9px;background:var(--blue);clip-path:polygon(50% 0,100% 25%,100% 75%,50% 100%,0 75%,0 25%)"></span><span style="font-size:3.3px">Write Simple Text</span></div>
    <div class="tx" style="margin-top:4px;color:#555">Lorem Ipsum is simply dummy text a print and typeset industry has text ever since the 1500s.</div>
  </div>
  <div class="foot"><div class="brand"><span class="dot" style="width:5px;height:5px"></span>KESTREL</div><div class="rule"></div><div class="num">3</div></div>
</section>

<!-- 5 Executive summary -->
<section class="slide" style="left:316px;top:199px">
  <div class="kicker" style="left:17px;top:12px">Summary of services offered by Kestrel Energy</div>
  <div class="eyebrow" style="left:17px;top:23px;font-size:9.5px">Executive</div>
  <div class="heading" style="left:17px;top:34px;font-size:15px">Summary</div>
  <div class="a" style="left:17px;top:61px;width:135px;display:grid;grid-template-columns:1fr 1fr;column-gap:8px;row-gap:8px">
    <div><div class="tb">Project Problem</div><div class="tx">Lorem ipsum dolor sit amet, cons ectetuer adipiscing elit, sed diam nonummy nibh euismod tincidunt ipsum dolor sit amet.</div></div>
    <div><div class="tb">Project Solution</div><div class="tx">Lorem ipsum dolor sit amet, cons ectetuer adipiscing elit, sed diam nonummy nibh euismod tincidunt ipsum dolor sit amet.</div></div>
    <div><div class="tb">Project Problem</div><div class="tx">Lorem ipsum dolor sit amet, cons ectetuer adipiscing elit, sed diam nonummy nibh euismod tincidunt ipsum dolor sit amet.</div></div>
    <div><div class="tb">Project Solution</div><div class="tx">Lorem ipsum dolor sit amet, cons ectetuer adipiscing elit, sed diam nonummy nibh euismod tincidunt ipsum dolor sit amet.</div></div>
  </div>
  <div class="a" style="left:161px;top:37px;width:86px;height:84px;display:grid;grid-template-columns:1fr 1fr;gap:2px;color:#fff">
    <div style="background:var(--blue);border-radius:4px 0 0 0;padding:16px 5px 0;font-size:3px"><b>PROBLEM</b><div style="font-size:2.2px;margin-top:4px">Lorem ipsum dolor sit amet, cons ectetuer adipiscing elit.</div></div>
    <div style="background:var(--green);border-radius:0 4px 0 0;padding:16px 5px 0;font-size:3px"><b>SOLUTION</b><div style="font-size:2.2px;margin-top:4px">Lorem ipsum dolor sit amet, cons ectetuer adipiscing elit.</div></div>
    <div style="background:var(--green);border-radius:0 0 0 4px;padding:14px 5px 0;font-size:3px"><b>MARKET</b><div style="font-size:2.2px;margin-top:4px">Lorem ipsum dolor sit amet, cons ectetuer adipiscing elit.</div></div>
    <div style="background:var(--blue);border-radius:0 0 4px 0;padding:14px 5px 0;font-size:3px"><b>MISSION</b><div style="font-size:2.2px;margin-top:4px">Lorem ipsum dolor sit amet, cons ectetuer adipiscing elit.</div></div>
  </div>
  <div class="foot"><div class="brand"><span class="dot" style="width:5px;height:5px"></span>KESTREL</div><div class="rule"></div><div class="num">4</div></div>
</section>

<!-- 6 Services -->
<section class="slide" style="left:596px;top:199px">
  <div class="eyebrow" style="left:13px;top:10px">Services offered</div>
  <div class="heading" style="left:13px;top:20px;font-size:11px">By Kestrel Energy</div>
  <div class="a" style="left:20px;top:39px;width:226px;height:78px;display:grid;grid-template-columns:1fr 1fr;grid-template-rows:1fr 1fr">
    <div style="background:var(--dark);display:flex;align-items:center;gap:8px;padding:0 6px"><span style="flex:none;width:26px;height:26px;border-radius:50%;background:#fff;border:2.5px solid var(--blue)"></span><div><div class="tb" style="color:#fff;font-size:4px">Business Strategy</div><div class="tx" style="color:#ccc">Lorem Ipsum is simply dummy text of the print and typesetting industry. Lorem Ipsum has the standard dummy text ever since the 1500s</div></div></div>
    <div style="background:var(--grey);display:flex;align-items:center;gap:8px;padding:0 6px"><span style="flex:none;width:26px;height:26px;border-radius:50%;background:var(--green)"></span><div><div class="tb" style="font-size:4px">Corporate Branding</div><div class="tx">Lorem Ipsum is simply dummy text of the print and typesetting industry. Lorem Ipsum has the standard dummy text ever since the 1500s</div></div></div>
    <div style="background:var(--grey);display:flex;align-items:center;gap:8px;padding:0 6px"><span style="flex:none;width:26px;height:26px;border-radius:50%;background:var(--green)"></span><div><div class="tb" style="font-size:4px">Marketing Research</div><div class="tx">Lorem Ipsum is simply dummy text of the print and typesetting industry. Lorem Ipsum has the standard dummy text ever since the 1500s</div></div></div>
    <div style="background:var(--grey);display:flex;align-items:center;gap:8px;padding:0 6px"><span style="flex:none;width:26px;height:26px;border-radius:50%;background:var(--blue)"></span><div><div class="tb" style="font-size:4px">Client Management</div><div class="tx">Lorem Ipsum is simply dummy text of the print and typesetting industry. Lorem Ipsum has the standard dummy text ever since the 1500s</div></div></div>
  </div>
  <div class="foot"><div class="brand"><span class="dot" style="width:5px;height:5px"></span>KESTREL</div><div class="rule"></div><div class="num">5</div></div>
</section>

<!-- 7 Oil fields list -->
<section class="slide" style="left:36px;top:363px">
  <div class="eyebrow" style="left:21px;top:19px">Summary</div>
  <div class="heading" style="left:21px;top:30px">List of oil fields</div>
  <div class="a" style="left:24px;top:50px;width:90px;display:grid;row-gap:9px">
    <div><div class="tb">◆ LOREM IPSUM</div><div class="tx" style="padding-left:5px">Lorem ipsumectetuer adipiscing elit, sed diam nonummy nibh euismod tincidunt</div></div>
    <div><div class="tb">◆ LOREM IPSUM</div><div class="tx" style="padding-left:5px">Lorem ipsumectetuer adipiscing elit, sed diam nonummy nibh euismod tincidunt</div></div>
    <div><div class="tb">◆ LOREM IPSUM</div><div class="tx" style="padding-left:5px">Lorem ipsumectetuer adipiscing elit, sed diam nonummy nibh euismod tincidunt</div></div>
  </div>
  <div class="a" style="left:129px;top:26px;width:130px;display:grid;grid-template-columns:1fr 1fr;row-gap:6px;text-align:center">
    <div><div style="margin:0 auto;width:19px;height:19px;border:1px solid var(--blue);padding:1.5px"><div style="width:100%;height:100%;background:var(--blue)"></div></div><div class="tb" style="font-size:3.4px;margin-top:3px">LOREM IPSUM</div><div class="tx" style="font-size:2.2px">Lorem ipsum dolor sit amet consectetuer adipiscing elit, sed diam nonummy nibh euismod</div></div>
    <div><div style="margin:0 auto;width:19px;height:19px;border:1px solid var(--green);padding:1.5px"><div style="width:100%;height:100%;background:var(--green)"></div></div><div class="tb" style="font-size:3.4px;margin-top:3px">LOREM IPSUM</div><div class="tx" style="font-size:2.2px">Lorem ipsum dolor sit amet consectetuer adipiscing elit, sed diam nonummy nibh euismod</div></div>
    <div><div style="margin:0 auto;width:19px;height:19px;border:1px solid var(--green);padding:1.5px"><div style="width:100%;height:100%;background:var(--green)"></div></div><div class="tb" style="font-size:3.4px;margin-top:3px">LOREM IPSUM</div><div class="tx" style="font-size:2.2px">Lorem ipsum dolor sit amet consectetuer adipiscing elit, sed diam nonummy nibh euismod</div></div>
    <div><div style="margin:0 auto;width:19px;height:19px;border:1px solid var(--blue);padding:1.5px"><div style="width:100%;height:100%;background:var(--blue)"></div></div><div class="tb" style="font-size:3.4px;margin-top:3px">LOREM IPSUM</div><div class="tx" style="font-size:2.2px">Lorem ipsum dolor sit amet consectetuer adipiscing elit, sed diam nonummy nibh euismod</div></div>
  </div>
  <div class="foot"><div class="brand"><span class="dot" style="width:5px;height:5px"></span>KESTREL</div><div class="rule"></div><div class="num">6</div></div>
</section>

<!-- 8 Key characteristics -->
<section class="slide" style="left:316px;top:363px">
  <div class="eyebrow" style="left:13px;top:11px">Kestrel Energy oil field key</div>
  <div class="heading" style="left:13px;top:22px;font-size:11px">Characteristics</div>
  <div class="a" style="left:21px;top:49px;width:80px;display:grid;row-gap:9px">
    <div><div class="tb">Lorem ipsum dolor.</div><div class="tx" style="font-size:3px">Lorem ipsumectetuer adipiscing elit, sed diam nonummy nibh euismod tincidunt</div></div>
    <div><div class="tb">Lorem ipsum dolor.</div><div class="tx" style="font-size:3px">Lorem ipsumectetuer adipiscing elit, sed diam nonummy nibh euismod tincidunt</div></div>
    <div><div class="tb">Lorem ipsum dolor.</div><div class="tx" style="font-size:3px">Lorem ipsumectetuer adipiscing elit, sed diam nonummy nibh euismod tincidunt</div></div>
  </div>
  <table class="a" style="left:113px;top:47px;width:133px;font-size:2.6px;text-align:center;color:#777">
    <tr style="height:12px;color:#fff;font-weight:600"><td style="background:var(--blue)">Main Text</td><td style="background:var(--green)">Main Text</td><td style="background:var(--blue)">Main Text</td><td style="background:var(--green)">Main Text</td></tr>
    <tr style="height:13px;border-bottom:.5px solid #333"><td>Text Here</td><td>Text Here</td><td>Text Here</td><td>Text Here</td></tr>
    <tr style="height:13px;border-bottom:.5px solid #333;background:#f4f4f4"><td>Text Here</td><td>Text Here</td><td>Text Here</td><td>Text Here</td></tr>
    <tr style="height:13px;border-bottom:.5px solid #333"><td>Text Here</td><td>Text Here</td><td>Text Here</td><td>Text Here</td></tr>
    <tr style="height:13px;border-bottom:.5px solid #333;background:#f4f4f4"><td>Text Here</td><td>Text Here</td><td>Text Here</td><td>Text Here</td></tr>
    <tr style="height:13px;border-bottom:.5px solid #333"><td>Text Here</td><td>Text Here</td><td>Text Here</td><td>Text Here</td></tr>
  </table>
  <div class="foot"><div class="brand"><span class="dot" style="width:5px;height:5px"></span>KESTREL</div><div class="rule"></div><div class="num">7</div></div>
</section>

<!-- 9 Partners -->
<section class="slide" style="left:596px;top:363px">
  <div class="eyebrow" style="left:13px;top:11px">Overview of</div>
  <div class="heading" style="left:13px;top:22px">Kestrel Energy partners</div>
  <div class="a" style="left:21px;top:43px;width:230px;display:grid;grid-template-columns:repeat(4,1fr);column-gap:8px">
    <div><div style="margin-left:3px;width:42px;height:23px;border:1px solid var(--blue);border-radius:4px;display:grid;place-items:center;font-size:4.5px;color:var(--dark)">LOGO</div><div class="tb" style="margin-top:6px;font-size:3.6px">Lorem ipsum dolor.</div><div class="tx" style="font-size:2.2px">Lorem ipsumectetuer adipiscing elit, sed diam nonummy nibh euismod tincidunt</div><div class="tx" style="font-size:2.2px;margin-top:4px">Lorem ipsumectetuer adipiscing elit, sed diam nonummy nibh euismod tincidunt Lorem ipsumectetuer adipiscing elit.</div></div>
    <div><div style="margin-left:3px;width:42px;height:23px;border:1px solid var(--blue);border-radius:4px;display:grid;place-items:center;font-size:4.5px;color:var(--dark)">LOGO</div><div class="tb" style="margin-top:6px;font-size:3.6px">Lorem ipsum dolor.</div><div class="tx" style="font-size:2.2px">Lorem ipsumectetuer adipiscing elit, sed diam nonummy nibh euismod tincidunt</div><div class="tx" style="font-size:2.2px;margin-top:4px">Lorem ipsumectetuer adipiscing elit, sed diam nonummy nibh euismod tincidunt Lorem ipsumectetuer adipiscing elit.</div></div>
    <div><div style="margin-left:3px;width:42px;height:23px;border:1px solid var(--blue);border-radius:4px;display:grid;place-items:center;font-size:4.5px;color:var(--dark)">LOGO</div><div class="tb" style="margin-top:6px;font-size:3.6px">Lorem ipsum dolor.</div><div class="tx" style="font-size:2.2px">Lorem ipsumectetuer adipiscing elit, sed diam nonummy nibh euismod tincidunt</div><div class="tx" style="font-size:2.2px;margin-top:4px">Lorem ipsumectetuer adipiscing elit, sed diam nonummy nibh euismod tincidunt Lorem ipsumectetuer adipiscing elit.</div></div>
    <div><div style="margin-left:3px;width:42px;height:23px;border:1px solid var(--blue);border-radius:4px;display:grid;place-items:center;font-size:4.5px;color:var(--dark)">LOGO</div><div class="tb" style="margin-top:6px;font-size:3.6px">Lorem ipsum dolor.</div><div class="tx" style="font-size:2.2px">Lorem ipsumectetuer adipiscing elit, sed diam nonummy nibh euismod tincidunt</div><div class="tx" style="font-size:2.2px;margin-top:4px">Lorem ipsumectetuer adipiscing elit, sed diam nonummy nibh euismod tincidunt Lorem ipsumectetuer adipiscing elit.</div></div>
  </div>
  <div class="foot"><div class="brand"><span class="dot" style="width:5px;height:5px"></span>KESTREL</div><div class="rule"></div><div class="num">8</div></div>
</section>

<!-- 10 Mission & values -->
<section class="slide" style="left:36px;top:525px">
  <div class="eyebrow" style="left:19px;top:16px">Kestrel Energy</div>
  <div class="heading" style="left:19px;top:27px">Mission &amp; Values</div>
  <div class="a tx" style="left:19px;top:39px;width:100px;font-size:3px">Lorem ipsum dolor sit amet, cons ectetuer adipiscing elit, sed diam nonummy nibh euismod tincidunt Lorem ipsum dolor sit amet.</div>
  <div class="media" role="img" aria-label="Gas processing plant with pipework under blue sky" style="left:19px;top:62px;width:100px;height:58px;border-radius:5px;background:linear-gradient(180deg,#5c9ed6 0%,#9fb8cc 50%,#6d7a86 100%)"></div>
  <div class="a" style="left:129px;top:35px;width:121px;height:39px;background:var(--grey);border-radius:5px"></div>
  <div class="a" style="left:129px;top:35px;width:28px;height:39px;background:var(--green);border-radius:5px"></div>
  <div class="a" style="left:169px;top:40px;width:76px"><div class="tb" style="font-size:5.5px">Mission</div><div class="tx" style="font-size:3px;margin-top:2px">Lorem ipsum dolor sit amet, cons ectetuer adipiscing elit, sed diam nonummy nibh euismod tincidunt.</div></div>
  <div class="a" style="left:129px;top:82px;width:121px;height:39px;background:var(--grey);border-radius:5px"></div>
  <div class="a" style="left:129px;top:82px;width:28px;height:39px;background:var(--blue);border-radius:5px"></div>
  <div class="a" style="left:169px;top:87px;width:76px"><div class="tb" style="font-size:5.5px">Values</div><div class="tx" style="font-size:3px;margin-top:2px">Lorem ipsum dolor sit amet, cons ectetuer adipiscing elit, sed diam nonummy nibh euismod tincidunt.</div></div>
  <div class="foot"><div class="brand"><span class="dot" style="width:5px;height:5px"></span>KESTREL</div><div class="rule"></div><div class="num">9</div></div>
</section>

<!-- 11 Health & safety -->
<section class="slide" style="left:316px;top:525px">
  <div class="eyebrow" style="left:13px;top:9px">Kestrel Energy health and</div>
  <div class="heading" style="left:13px;top:20px">Safety strategy</div>
  <div class="a" role="img" aria-label="Faint world map backdrop" style="left:38px;top:34px;width:196px;height:96px;border-radius:40%;background:radial-gradient(#eef0f1,#fff 75%)"></div>
  <svg class="a" style="left:0;top:0" width="266" height="150" viewBox="0 0 266 150">
    <g fill="#fff" stroke="#2b2d2f" stroke-width="1.4">
      <rect x="49" y="47" width="54" height="68" rx="5"/>
      <rect x="111" y="47" width="54" height="68" rx="5"/>
      <rect x="172" y="47" width="54" height="68" rx="5"/>
    </g>
    <g fill="#2b2d2f"><circle cx="93" cy="64" r="2"/><circle cx="155" cy="64" r="2"/><circle cx="121" cy="98" r="2"/><circle cx="182" cy="98" r="2"/></g>
    <circle cx="76" cy="63" r="3.5" fill="none" stroke="#0a8dd6" stroke-width=".8"/>
    <rect x="133" y="60" width="9" height="6" fill="none" stroke="#0a8dd6" stroke-width=".8"/>
    <polyline points="195,67 198,63 201,65 205,60" fill="none" stroke="#12a57c" stroke-width=".9"/>
  </svg>
  <div class="a" style="left:49px;top:73px;width:54px;text-align:center"><div style="font-size:3.6px;font-weight:700;color:var(--green)">IDEA</div><div class="tx" style="font-size:2px;padding:0 5px">Lorem ipsum dolor sit amet, consectetuer adipiscing elit, sed diam nonummy nibh euismod tincidunt ut laoreet dolore magna aliquam erat volutpat.</div></div>
  <div class="a" style="left:111px;top:73px;width:54px;text-align:center"><div style="font-size:3.6px;font-weight:700;color:var(--green)">PROMOTION</div><div class="tx" style="font-size:2px;padding:0 5px">Lorem ipsum dolor sit amet, consectetuer adipiscing elit, sed diam nonummy nibh euismod tincidunt ut laoreet dolore magna aliquam erat volutpat.</div></div>
  <div class="a" style="left:172px;top:73px;width:54px;text-align:center"><div style="font-size:3.6px;font-weight:700;color:var(--green)">GROWTH</div><div class="tx" style="font-size:2px;padding:0 5px">Lorem ipsum dolor sit amet, consectetuer adipiscing elit, sed diam nonummy nibh euismod tincidunt ut laoreet dolore magna aliquam erat volutpat.</div></div>
  <div class="foot"><div class="brand"><span class="dot" style="width:5px;height:5px"></span>KESTREL</div><div class="rule"></div><div class="num">10</div></div>
</section>

<!-- 12 Environmental strategy -->
<section class="slide" style="left:596px;top:525px">
  <div class="a" style="left:124px;top:0;width:142px;height:62px;background:var(--dark);border-radius:0 0 0 18px"></div>
  <div class="media" role="img" aria-label="Offshore worker in hard hat on platform at sunset" style="left:160px;top:16px;width:91px;height:94px;background:linear-gradient(180deg,#6e5a4b 0%,#e07a2c 45%,#3e3a38 100%)"></div>
  <div class="a" style="left:136px;top:110px;width:130px;height:22px;background:var(--blue);display:flex;align-items:center;color:#fff;font-weight:800">
    <span style="width:22px;height:22px;background:var(--green)"></span>
    <span style="width:55px;text-align:center;font-size:11px;border-right:.6px solid #fff">100K</span>
    <span style="flex:1;text-align:center;font-size:11px">+1M</span>
  </div>
  <div class="a" style="left:14px;top:14px;font-size:6px;font-weight:700;color:var(--dark)">KESTREL ENERGY</div>
  <div class="eyebrow" style="left:14px;top:24px;font-size:10px">Environmental</div>
  <div class="heading" style="left:14px;top:36px;font-size:13.5px">Strategy</div>
  <div class="a tx" style="left:14px;top:55px;width:100px;font-size:3.4px;color:#555">Lorem ipsum dolor sit amet consect adipisc elit incididunt labore dolore aliqua.</div>
  <div class="a" style="left:30px;top:75px;width:90px"><div class="tb" style="font-size:5.5px;display:flex;gap:3px;align-items:center"><span style="width:6px;height:6px;background:var(--green);border-radius:1px"></span>Make Simple Text</div><div class="tx" style="font-size:2.4px;color:#555;margin-top:2px">Nemo enim ipsam voluptatem quia voluptas aspernat fugit sed quia magni dolore ratione is voluptas neque porro quisquam sequi nesciunt.</div></div>
  <div class="a" style="left:30px;top:107px;width:90px"><div class="tb" style="font-size:5.5px;display:flex;gap:3px;align-items:center"><span style="width:6px;height:6px;background:var(--green);border-radius:1px"></span>Make Simple Text</div><div class="tx" style="font-size:2.4px;color:#555;margin-top:2px">Nemo enim ipsam voluptatem quia voluptas aspernat fugit sed quia magni dolore ratione voluptas.</div></div>
  <div class="foot"><div class="brand"><span class="dot" style="width:5px;height:5px"></span>KESTREL</div><div class="rule"></div><div class="num">11</div></div>
</section>

<!-- 13 Benefits -->
<section class="slide" style="left:36px;top:688px">
  <div class="media" role="img" aria-label="Engineer in hi-vis jacket and hard hat facing an industrial plant" style="left:24px;top:17px;width:98px;height:107px;border-radius:6px;background:linear-gradient(180deg,#4a6d88 0%,#d18a2c 55%,#3b3633 100%)"></div>
  <div class="eyebrow" style="left:137px;top:20px;font-size:8px">Benefits</div>
  <div class="heading" style="left:137px;top:30px;font-size:11.5px">To society</div>
  <div class="a" style="left:139px;top:47px;font-size:3.3px;font-weight:600;color:var(--dark)">(job creation, more revenue for the government, etc)</div>
  <div class="a" style="left:138px;top:59px;width:110px;display:grid;row-gap:6px">
    <div style="display:flex;gap:4px"><span style="flex:none;width:6px;height:6px;border:.8px solid var(--green);border-radius:1px"></span><div><div class="tb" style="font-size:3.4px">Lorem ipsum dolor.</div><div class="tx" style="font-size:3px;color:#555">Lorem ipsumectetuer adipiscing elit, sed diam nonummy nibh euismod tincidunt</div></div></div>
    <div style="display:flex;gap:4px"><span style="flex:none;width:6px;height:6px;border:.8px solid var(--green);border-radius:50%"></span><div><div class="tb" style="font-size:3.4px">Lorem ipsum dolor.</div><div class="tx" style="font-size:3px;color:#555">Lorem ipsumectetuer adipiscing elit, sed diam nonummy nibh euismod tincidunt</div></div></div>
    <div style="display:flex;gap:4px"><span style="flex:none;width:6px;height:6px;border:.8px solid var(--green);transform:rotate(45deg) scale(.8)"></span><div><div class="tb" style="font-size:3.4px">Lorem ipsum dolor.</div><div class="tx" style="font-size:3px;color:#555">Lorem ipsumectetuer adipiscing elit, sed diam nonummy nibh euismod tincidunt</div></div></div>
  </div>
  <div class="foot"><div class="brand"><span class="dot" style="width:5px;height:5px"></span>KESTREL</div><div class="rule"></div><div class="num">12</div></div>
</section>

<!-- 14 Geographic coverage -->
<section class="slide" style="left:316px;top:688px">
  <div class="eyebrow" style="left:13px;top:10px;font-size:7.5px">Kestrel Energy</div>
  <div class="eyebrow" style="left:13px;top:19px;font-size:7.5px">Geographic coverage</div>
  <div class="heading" style="left:13px;top:29px;font-size:11px">In Central Africa</div>
  <div class="a" role="img" aria-label="Map of Africa with location pins" style="left:150px;top:14px;width:98px;height:122px;border-radius:40% 45% 50% 35%;background:linear-gradient(160deg,#e4e6e8,#d5d8db)"></div>
  <svg class="a" style="left:0;top:0" width="266" height="150" viewBox="0 0 266 150">
    <g fill="#2b2d2f"><path d="M176 18a3 3 0 1 1 0 .1zM176 21l-2.5-3h5z"/><path d="M209 107a3 3 0 1 1 0 .1zM209 110l-2.5-3h5z"/></g>
    <g fill="var(--green)"><circle cx="170" cy="40" r="2.6"/><circle cx="236" cy="92" r="2.6"/></g>
    <g fill="var(--blue)"><circle cx="215" cy="48" r="2.6"/><circle cx="197" cy="100" r="2.6"/></g>
    <polygon points="18,41 64,41 70,46 64,51 18,51" fill="var(--green)"/>
    <polygon points="18,68 64,68 70,73 64,78 18,78" fill="var(--blue)"/>
    <polygon points="18,96 64,96 70,101 64,106 18,106" fill="var(--dark)"/>
  </svg>
  <div class="a" style="left:20px;top:43px;font-size:5px;font-weight:800;color:#fff">1 <span style="font-size:2.4px;vertical-align:middle;padding-left:3px">LOREM IPSUM</span></div>
  <div class="a" style="left:20px;top:70px;font-size:5px;font-weight:800;color:#fff">2 <span style="font-size:2.4px;vertical-align:middle;padding-left:3px">LOREM IPSUM</span></div>
  <div class="a" style="left:20px;top:98px;font-size:5px;font-weight:800;color:#fff">3 <span style="font-size:2.4px;vertical-align:middle;padding-left:3px">LOREM IPSUM</span></div>
  <div class="a tx" style="left:18px;top:55px;width:95px;font-size:3px">Lorem ipsum dolor sit amet, consectetur adipiscing elit, sed do eiusmod tempor.</div>
  <div class="a tx" style="left:18px;top:82px;width:95px;font-size:3px">Lorem ipsum dolor sit amet, consectetur adipiscing elit, sed do eiusmod tempor.</div>
  <div class="a tx" style="left:18px;top:110px;width:95px;font-size:3px">Lorem ipsum dolor sit amet, consectetur adipiscing elit, sed do eiusmod tempor.</div>
  <div class="a" style="left:145px;top:70px;width:40px;text-align:center"><div style="font-size:7.5px;font-weight:600;color:var(--dark)">+ 24530</div><div class="tx" style="font-size:2.2px;color:#aaa">Lorem ipsum is simply dummy text of the printing and typesetting</div></div>
  <div class="foot"><div class="brand"><span class="dot" style="width:5px;height:5px"></span>KESTREL</div><div class="rule"></div><div class="num">13</div></div>
</section>

<!-- 15 Shareholders -->
<section class="slide" style="left:596px;top:688px">
  <div class="eyebrow" style="left:9px;top:10px">Kestrel Energy</div>
  <div class="heading" style="left:9px;top:20px">Shareholders' structure</div>
  <div class="a tx" style="left:9px;top:32px;width:130px;font-size:3px;color:#444">Lorem ipsum dolor sit amet, cons ectetuer adipiscing sed diam nonummy nibh euismod tincidunt.Lorem ipsum dolor sit amet.</div>
  <svg class="a" style="left:0;top:0" width="266" height="150" viewBox="0 0 266 150">
    <g transform="translate(85,88)" stroke="#fff" stroke-width="1.6" stroke-linejoin="round">
      <path d="M0 0L0 -38A38 38 0 0 1 22.3 -30.7Z" fill="var(--green)" transform="translate(1.2,-1.5)"/>
      <path d="M0 0L22.3 -30.7A38 38 0 0 1 38 0Z" fill="#3b3d40" transform="translate(2,0)"/>
      <path d="M0 0L38 0A38 38 0 0 1 -11.7 36.1Z" fill="#b3b5b8" transform="translate(0,2)"/>
      <path d="M0 0L-11.7 36.1A38 38 0 0 1 0 -38Z" fill="var(--blue)" transform="translate(-2,0)"/>
    </g>
    <g fill="#fff" font-family="Poppins,sans-serif" font-weight="700" font-size="7">
      <text x="89" y="66">10%</text><text x="102" y="92">15%</text><text x="82" y="115">30%</text><text x="57" y="87">45%</text>
    </g>
  </svg>
  <div class="a" style="left:136px;top:49px;width:125px;display:grid;row-gap:6px">
    <div style="display:flex;gap:4px;align-items:center"><span style="flex:none;width:11px;height:11px;border-radius:50%;background:var(--blue);color:#fff;font-size:4px;display:grid;place-items:center">01</span><div><div class="tb" style="font-size:3.4px">Shareholders Name</div><div class="tx" style="font-size:2.2px">Lorem ipsum dolor sit amet, consectetuer adipiscing elit, sed do eiusmod tempor incididunt ut labore et dolore magna aliqua.</div></div></div>
    <div style="display:flex;gap:4px;align-items:center;padding-left:9px"><span style="flex:none;width:11px;height:11px;border-radius:50%;background:var(--green);color:#fff;font-size:4px;display:grid;place-items:center">02</span><div><div class="tb" style="font-size:3.4px">Shareholders Name</div><div class="tx" style="font-size:2.2px">Lorem ipsum dolor sit amet, consectetuer adipiscing elit, sed do eiusmod tempor incididunt ut labore et dolore magna aliqua.</div></div></div>
    <div style="display:flex;gap:4px;align-items:center;padding-left:9px"><span style="flex:none;width:11px;height:11px;border-radius:50%;background:#3b3d40;color:#fff;font-size:4px;display:grid;place-items:center">03</span><div><div class="tb" style="font-size:3.4px">Shareholders Name</div><div class="tx" style="font-size:2.2px">Lorem ipsum dolor sit amet, consectetuer adipiscing elit, sed do eiusmod tempor incididunt ut labore et dolore magna aliqua.</div></div></div>
    <div style="display:flex;gap:4px;align-items:center"><span style="flex:none;width:11px;height:11px;border-radius:50%;background:#b3b5b8;color:#fff;font-size:4px;display:grid;place-items:center">04</span><div><div class="tb" style="font-size:3.4px">Shareholders Name</div><div class="tx" style="font-size:2.2px">Lorem ipsum dolor sit amet, consectetuer adipiscing elit, sed do eiusmod tempor incididunt ut labore et dolore magna aliqua.</div></div></div>
  </div>
  <div class="foot"><div class="brand"><span class="dot" style="width:5px;height:5px"></span>KESTREL</div><div class="rule"></div><div class="num">14</div></div>
</section>

<!-- 16 Organisational structure -->
<section class="slide" style="left:36px;top:851px">
  <div class="eyebrow" style="left:9px;top:11px">Kestrel Energy</div>
  <div class="heading" style="left:9px;top:22px">Organisational structure</div>
  <div class="a tx" style="left:9px;top:33px;width:240px;font-size:3px;color:#444">Lorem ipsum dolor sit amet, cons ectetuer adipiscing elit, sed diam nonummy nibh euismod tincidunt</div>
  <svg class="a" style="left:0;top:0" width="266" height="150" viewBox="0 0 266 150">
    <g stroke="#555" stroke-width=".5" fill="none">
      <path d="M133 63V70M57 70H209M57 70V77M133 70V77M209 70V77"/>
      <path d="M57 99V104M44 104H69M44 104V110M69 104V110"/>
      <path d="M133 99V104M121 104H146M121 104V110M146 104V110"/>
      <path d="M209 99V104M197 104H222M197 104V110M222 104V110"/>
    </g>
    <g fill="#e3e4e6">
      <circle cx="133" cy="51" r="8" stroke="var(--blue)" stroke-width="2"/>
      <circle cx="57" cy="86" r="8" stroke="var(--green)" stroke-width="2"/>
      <circle cx="133" cy="86" r="8" stroke="var(--green)" stroke-width="2"/>
      <circle cx="209" cy="86" r="8" stroke="var(--green)" stroke-width="2"/>
      <g stroke="#999" stroke-width="1"><circle cx="44" cy="117" r="5.5"/><circle cx="69" cy="117" r="5.5"/><circle cx="121" cy="117" r="5.5"/><circle cx="146" cy="117" r="5.5"/><circle cx="197" cy="117" r="5.5"/><circle cx="222" cy="117" r="5.5"/></g>
    </g>
    <g font-family="Poppins,sans-serif" font-size="1.9" font-weight="700" fill="#222" text-anchor="middle">
      <text x="133" y="63">NAME SURNAME</text><text x="57" y="98">NAME SURNAME</text><text x="133" y="98">NAME SURNAME</text><text x="209" y="98">NAME SURNAME</text>
      <text x="44" y="126">NAME SURNAME</text><text x="69" y="126">NAME SURNAME</text><text x="121" y="126">NAME SURNAME</text><text x="146" y="126">NAME SURNAME</text><text x="197" y="126">NAME SURNAME</text><text x="222" y="126">NAME SURNAME</text>
    </g>
  </svg>
  <div class="foot"><div class="brand"><span class="dot" style="width:5px;height:5px"></span>KESTREL</div><div class="rule"></div><div class="num">15</div></div>
</section>

<!-- 17 Management -->
<section class="slide" style="left:316px;top:851px">
  <div class="eyebrow" style="left:13px;top:14px;font-size:7.5px">Kestrel Energy</div>
  <div class="heading" style="left:13px;top:24px;font-size:12px">Management</div>
  <svg class="a" style="left:0;top:0" width="266" height="150" viewBox="0 0 266 150">
    <g transform="translate(136,82)">
      <path d="M-37 0A37 37 0 0 1 0 -37V-21A21 21 0 0 0 -21 0Z" fill="var(--blue)"/>
      <path d="M0 -37A37 37 0 0 1 37 0H21A21 21 0 0 0 0 -21Z" fill="var(--green)"/>
      <path d="M37 0A37 37 0 0 1 0 37V21A21 21 0 0 0 21 0Z" fill="var(--blue)"/>
      <path d="M0 37A37 37 0 0 1 -37 0H-21A21 21 0 0 0 0 21Z" fill="var(--green)"/>
      <g fill="none" stroke="#fff" stroke-width=".9"><circle cx="-17" cy="-17" r="4"/><circle cx="17" cy="-17" r="4"/><circle cx="17" cy="17" r="4"/><circle cx="-17" cy="17" r="4"/></g>
    </g>
  </svg>
  <div class="a" style="left:116px;top:74px;width:40px;text-align:center;font-size:7px;font-weight:700;line-height:1;color:var(--dark)">Text<br>Added</div>
  <div class="a" style="left:30px;top:44px;width:62px;text-align:right"><div class="tb" style="font-size:5px">Text Here</div><div class="tx" style="font-size:2.4px;color:#555">Lorem ipsum dolor sit amet, consectetuer adipiscing elit, sed diammy nibh euismod tincidunt ut laoreet dolore</div></div>
  <div class="a" style="left:30px;top:97px;width:62px;text-align:right"><div class="tb" style="font-size:5px">Text Here</div><div class="tx" style="font-size:2.4px;color:#555">Lorem ipsum dolor sit amet, consectetuer adipiscing elit, sed diammy nibh euismod tincidunt ut laoreet dolore</div></div>
  <div class="a" style="left:180px;top:44px;width:62px"><div class="tb" style="font-size:5px">Text Here</div><div class="tx" style="font-size:2.4px;color:#555">Lorem ipsum dolor sit amet, consectetuer adipiscing elit, sed diammy nibh euismod tincidunt ut laoreet dolore</div></div>
  <div class="a" style="left:180px;top:97px;width:62px"><div class="tb" style="font-size:5px">Text Here</div><div class="tx" style="font-size:2.4px;color:#555">Lorem ipsum dolor sit amet, consectetuer adipiscing elit, sed diammy nibh euismod tincidunt ut laoreet dolore</div></div>
  <div class="foot"><div class="brand"><span class="dot" style="width:5px;height:5px"></span>KESTREL</div><div class="rule"></div><div class="num">16</div></div>
</section>

<!-- 18 Board of directors -->
<section class="slide" style="left:596px;top:851px">
  <div class="eyebrow" style="left:13px;top:14px;font-size:7.5px">Kestrel Energy</div>
  <div class="heading" style="left:13px;top:24px;font-size:11.5px">Board of directors</div>
  <div class="a" style="left:26px;top:43px;width:220px;display:grid;grid-template-columns:repeat(3,1fr);text-align:center">
    <div><div role="img" aria-label="Portrait photo placeholder" style="margin:0 auto;width:42px;height:42px;background:#e5e6e8;border:1.5px solid #eee;border-bottom:3px solid var(--blue)"></div><div style="font-size:4px;font-weight:700;color:var(--blue);margin-top:6px">DANIEL MOORE</div><div style="font-size:2.4px;font-weight:600">Managing Director</div><div class="tx" style="font-size:2px;padding:1px 10px">Lorem text is simply dummy text of print &amp; typeset industry. Lorem has been standard dummy text ever.</div><div style="display:flex;gap:3px;justify-content:center;margin-top:2px"><span style="width:4px;height:4px;border-radius:50%;border:1px solid var(--blue)"></span><span style="width:4px;height:4px;border-radius:50%;border:1px solid var(--blue)"></span><span style="width:4px;height:4px;border-radius:50%;border:1px solid var(--blue)"></span></div></div>
    <div><div role="img" aria-label="Portrait photo placeholder" style="margin:0 auto;width:42px;height:42px;background:#e5e6e8;border:1.5px solid #eee;border-bottom:3px solid var(--blue)"></div><div style="font-size:4px;font-weight:700;color:var(--blue);margin-top:6px">PETER LANG</div><div style="font-size:2.4px;font-weight:600">UI/UX Designer</div><div class="tx" style="font-size:2px;padding:1px 10px">Lorem text is simply dummy text of print &amp; typeset industry. Lorem has been standard dummy text ever.</div><div style="display:flex;gap:3px;justify-content:center;margin-top:2px"><span style="width:4px;height:4px;border-radius:50%;border:1px solid var(--blue)"></span><span style="width:4px;height:4px;border-radius:50%;border:1px solid var(--blue)"></span><span style="width:4px;height:4px;border-radius:50%;border:1px solid var(--blue)"></span></div></div>
    <div><div role="img" aria-label="Portrait photo placeholder" style="margin:0 auto;width:42px;height:42px;background:#e5e6e8;border:1.5px solid #eee;border-bottom:3px solid var(--blue)"></div><div style="font-size:4px;font-weight:700;color:var(--blue);margin-top:6px">SIMON GREY</div><div style="font-size:2.4px;font-weight:600">Web Developer</div><div class="tx" style="font-size:2px;padding:1px 10px">Lorem text is simply dummy text of print &amp; typeset industry. Lorem has been standard dummy text ever.</div><div style="display:flex;gap:3px;justify-content:center;margin-top:2px"><span style="width:4px;height:4px;border-radius:50%;border:1px solid var(--blue)"></span><span style="width:4px;height:4px;border-radius:50%;border:1px solid var(--blue)"></span><span style="width:4px;height:4px;border-radius:50%;border:1px solid var(--blue)"></span></div></div>
  </div>
  <div class="foot"><div class="brand"><span class="dot" style="width:5px;height:5px"></span>KESTREL</div><div class="rule"></div><div class="num">17</div></div>
</section>

<!-- 19 Timeline -->
<section class="slide" style="left:36px;top:1015px">
  <div class="eyebrow" style="left:10px;top:14px;font-size:7.5px">Kestrel Energy project</div>
  <div class="heading" style="left:10px;top:24px;font-size:11.5px">Deployment timeline</div>
  <svg class="a" style="left:0;top:0" width="266" height="150" viewBox="0 0 266 150">
    <g fill="var(--blue)"><polygon points="26,89 30,82 72,82 68,89"/><polygon points="111,82 153,82 149,89 107,89"/><polygon points="196,82 236,82 240,89 192,89"/></g>
    <g fill="var(--green)"><polygon points="70,89 74,82 109,82 105,89"/><polygon points="155,82 194,82 190,89 151,89"/></g>
    <g stroke="#222" stroke-width=".8"><path d="M49 67V80M134 67V80M219 67V80M91 91V104M177 91V104"/></g>
    <g fill="#222"><circle cx="49" cy="67" r="1.2"/><circle cx="134" cy="67" r="1.2"/><circle cx="219" cy="67" r="1.2"/><circle cx="91" cy="104" r="1.2"/><circle cx="177" cy="104" r="1.2"/></g>
    <g fill="#fff" font-family="Poppins,sans-serif" font-size="3.6" font-weight="600" text-anchor="middle"><text x="49" y="87">1990</text><text x="91" y="87">2001</text><text x="132" y="87">2007</text><text x="174" y="87">2012</text><text x="216" y="87">2020</text></g>
  </svg>
  <div class="a" style="left:29px;top:48px;width:40px;text-align:center"><div class="tb" style="font-size:4.4px;font-weight:500">Your Title</div><div class="tx" style="font-size:3px">Refers to a good or service being offered</div></div>
  <div class="a" style="left:114px;top:48px;width:40px;text-align:center"><div class="tb" style="font-size:4.4px;font-weight:500">Your Title</div><div class="tx" style="font-size:3px">Refers to a good or service being offered</div></div>
  <div class="a" style="left:199px;top:48px;width:40px;text-align:center"><div class="tb" style="font-size:4.4px;font-weight:500">Your Title</div><div class="tx" style="font-size:3px">Refers to a good or service being offered</div></div>
  <div class="a" style="left:71px;top:111px;width:40px;text-align:center"><div class="tb" style="font-size:4.4px;font-weight:500">Your Title</div><div class="tx" style="font-size:3px">Refers to a good or service being offered</div></div>
  <div class="a" style="left:157px;top:111px;width:40px;text-align:center"><div class="tb" style="font-size:4.4px;font-weight:500">Your Title</div><div class="tx" style="font-size:3px">Refers to a good or service being offered</div></div>
  <div class="foot"><div class="brand"><span class="dot" style="width:5px;height:5px"></span>KESTREL</div><div class="rule"></div><div class="num">18</div></div>
</section>

<!-- 20 Financial overview -->
<section class="slide" style="left:316px;top:1015px">
  <div class="eyebrow" style="left:11px;top:14px;font-size:8px">Kestrel Energy financial overview with</div>
  <div class="heading" style="left:11px;top:25px;font-size:12px">Comments on the financial</div>
  <table class="a" style="left:22px;top:42px;width:213px;font-size:2.6px;text-align:center;color:#333;font-weight:500">
    <tr style="height:12px"><td style="width:62px;background:var(--blue);border:1px solid #fff"></td><td style="background:var(--green);color:#fff;border:1px solid #fff">Your Text Here</td><td style="background:var(--green);color:#fff;border:1px solid #fff">Your Text Here</td><td style="background:var(--green);color:#fff;border:1px solid #fff">Your Text Here</td><td style="background:var(--green);color:#fff;border:1px solid #fff">Your Text Here</td></tr>
    <tr style="height:14px;background:#f3f3f3"><td style="background:var(--blue);color:#fff;border:1px solid #fff">You can replace this text</td><td>2020</td><td>1</td><td>50%</td><td>1250</td></tr>
    <tr style="height:14px"><td style="background:var(--blue);color:#fff;border:1px solid #fff">You can replace this text</td><td>2021</td><td>2</td><td>50%</td><td>3623</td></tr>
    <tr style="height:14px;background:#f3f3f3"><td style="background:var(--blue);color:#fff;border:1px solid #fff">You can replace this text</td><td>2022</td><td>3</td><td>12%</td><td>2549</td></tr>
    <tr style="height:14px"><td style="background:var(--blue);color:#fff;border:1px solid #fff">You can replace this text</td><td>2023</td><td>4</td><td>65%</td><td>1020</td></tr>
    <tr style="height:14px;background:#f3f3f3"><td style="background:var(--blue);color:#fff;border:1px solid #fff">You can replace this text</td><td>2024</td><td>5</td><td>65%</td><td>1020</td></tr>
  </table>
  <div class="foot"><div class="brand"><span class="dot" style="width:5px;height:5px"></span>KESTREL</div><div class="rule"></div><div class="num">19</div></div>
</section>

<!-- 21 Contact -->
<section class="slide" style="left:596px;top:1015px">
  <div class="a" style="left:80px;top:26px;display:flex;align-items:center;gap:4px">
    <span class="dot" style="width:20px;height:20px"></span>
    <span style="font-size:11px;font-weight:800;color:var(--blue);line-height:1">KESTREL<br>ENERGY</span>
  </div>
  <div class="a" style="left:19px;top:65px;width:228px;height:42px;background:var(--green);border-radius:5px;color:#fff">
    <div style="text-align:center;font-size:11px;font-weight:800;margin-top:5px">CONTACT US</div>
    <div style="display:flex;justify-content:space-around;margin-top:4px;font-size:3.6px;line-height:1.3">
      <div style="display:flex;gap:3px;align-items:center"><span style="width:6px;height:6px;border-radius:50%;background:#fff"></span><span>Address Street Name<br>City Name, Country 000</span></div>
      <div style="display:flex;gap:3px;align-items:center"><span style="width:6px;height:6px;border-radius:50%;background:#fff"></span><span>(+000) 123 456 789<br>(+000) 123 456 789</span></div>
      <div style="display:flex;gap:3px;align-items:center"><span style="width:6px;height:6px;border-radius:50%;background:#fff"></span><span>Info@example.com<br>Www.example.com</span></div>
    </div>
  </div>
  <div class="a" style="left:0;width:266px;top:121px;text-align:center;font-size:5px;letter-spacing:2px;color:var(--blue)">www.website.com</div>
</section>

</div>
</body>
</html>
```